construction co.logo(ie.highway,heavy equip)

need a design for a new construction company in washington state,office is located on the water (beach front)also use a 1952 halvorn dune vesper as portable office,or the standard bold construction type logo's,these are just thoughts and not necassarily direction

Target Market(s)

I will be working as a sub to much larger general contractors and am looking for a strong,stable appearance.

Industry/Entity Type

Construction

```html
<!DOCTYPE html>
<html lang="en">
<head>
<meta charset="utf-8">
<title>Tideline General Contractors – Business Cards</title>
<link rel="stylesheet" href="https://fonts.googleapis.com/css2?family=Arimo:ital,wght@0,400;0,700;1,400&display=swap">
<style>
  :root {
    --page: #ffffff;
    --ink: #111111;
    --muted: #8f8f8f;
    --peach-light: #fbe6c4;
    --peach-mid: #f8c8a6;
    --palm-gold: #f4b400;
    --palm-light: #ffd84a;
    --sky-top: #2ed3e6;
    --sky-bottom: #ffffff;
    --band-blue: #1730e0;
    --band-yellow: #ffe800;
    --machine-yellow: #f2b21a;
    --white: #ffffff;
  }
  html, body {
    margin: 0;
    padding: 0;
    width: 1200px;
    height: 811px;
    overflow: hidden;
    background: var(--page);
    font-family: "Arimo", Arial, sans-serif;
  }
  .canvas {
    position: relative;
    width: 1200px;
    height: 811px;
  }

  /* Landscape card */
  .card-landscape {
    position: absolute;
    left: 80px;
    top: 88px;
    width: 584px;
    height: 356px;
    overflow: hidden;
  }
  .card-landscape .backdrop {
    position: absolute;
    inset: 0;
    background: radial-gradient(circle at 28% 55%, var(--peach-light) 0%, var(--peach-light) 25%, var(--peach-mid) 100%);
  }
  .card-landscape .palm-art {
    position: absolute;
    left: 40px;
    top: 8px;
    width: 160px;
    height: 348px;
    border-radius: 45% 45% 10% 10%;
    background: radial-gradient(ellipse at 50% 30%, var(--palm-light), var(--palm-gold) 65%, rgba(244,180,0,0) 100%);
  }
  .card-landscape .brand {
    position: absolute;
    left: 214px;
    top: 62px;
    margin: 0;
    color: var(--ink);
    font-weight: 400;
    font-size: 48px;
    line-height: 1;
  }
  .card-landscape .brand span {
    display: block;
    font-size: 16px;
    letter-spacing: 2.6px;
    color: var(--muted);
    margin-top: 6px;
  }
  .card-landscape .person {
    position: absolute;
    left: 214px;
    top: 176px;
  }
  .person .name {
    margin: 0;
    font-size: 25px;
    color: var(--ink);
  }
  .person .role {
    margin: 2px 0 0;
    font-size: 20px;
    font-style: italic;
    color: #333;
  }
  .card-landscape .contact {
    position: absolute;
    left: 214px;
    top: 256px;
    margin: 0;
    font-size: 18.5px;
    line-height: 24px;
    font-style: normal;
    color: var(--ink);
  }

  /* Portrait card */
  .card-portrait {
    position: absolute;
    left: 724px;
    top: 86px;
    width: 356px;
    height: 586px;
    overflow: hidden;
    background: linear-gradient(to bottom, var(--sky-top) 0%, #9fecf4 45%, var(--sky-bottom) 78%);
  }
  .card-portrait .machine-art {
    position: absolute;
    left: 22px;
    top: 6px;
    width: 310px;
    height: 150px;
    border-radius: 60% 40% 8% 8%;
    background: linear-gradient(160deg, #f7c94a, var(--machine-yellow) 60%, #c98a10);
  }
  .card-portrait .brand {
    position: absolute;
    left: 20px;
    top: 156px;
    margin: 0;
    color: var(--band-blue);
    font-weight: 700;
    font-size: 44px;
    line-height: 1;
  }
  .card-portrait .brand span {
    display: block;
    font-size: 28px;
    color: var(--ink);
    margin-top: 4px;
  }
  .card-portrait .person {
    position: absolute;
    left: 24px;
    top: 308px;
  }
  .card-portrait .person .name {
    font-weight: 700;
    padding-bottom: 4px;
    border-bottom: 1.5px solid var(--ink);
    width: 150px;
  }
  .card-portrait .person .role {
    margin-top: 6px;
    padding-bottom: 4px;
    border-bottom: 1.5px solid var(--ink);
    width: 150px;
  }
  .card-portrait .band {
    position: absolute;
    left: 0;
    top: 0;
    width: 356px;
    height: 586px;
  }
  .card-portrait .contact {
    position: absolute;
    left: 28px;
    top: 484px;
    margin: 0;
    font-size: 18px;
    line-height: 22px;
    font-style: normal;
    color: var(--white);
    transform: rotate(-3deg);
    transform-origin: left top;
  }
</style>
</head>
<body>
<main class="canvas">

  <section class="card-landscape" aria-label="Landscape business card">
    <div class="backdrop" role="img" aria-label="Soft peach sunburst background"></div>
    <div class="palm-art" role="img" aria-label="Golden palm trees illustration"></div>
    <h1 class="brand">Tideline <span>GENERAL CONTRACTORS</span></h1>
    <div class="person">
      <p class="name">Dale Merrow</p>
      <p class="role">Owner</p>
    </div>
    <address class="contact">
      48 Harbor Lane<br>
      Port Elden WA 98011,<br>
      office@tidelinebuilds.com<br>
      Phone 360-555-0142
    </address>
  </section>

  <section class="card-portrait" aria-label="Portrait business card">
    <div class="machine-art" role="img" aria-label="Yellow excavator illustration"></div>
    <h2 class="brand">Tideline <span>General Contractors</span></h2>
    <div class="person">
      <p class="name">Dale Merrow</p>
      <p class="role">Owner</p>
    </div>
    <svg class="band" viewBox="0 0 356 586" aria-hidden="true">
      <polygon points="0,460 356,430 356,586 0,586" fill="var(--band-yellow)"/>
      <polygon points="0,470 356,440 356,586 0,586" fill="var(--band-blue)"/>
    </svg>
    <address class="contact">
      48 Harbor Lane<br>
      Port Elden WA 98011,<br>
      office@tidelinebuilds.com<br>
      Phone 360-555-0142
    </address>
  </section>

</main>
</body>
</html>
```